Lumo -Fresh business card design

It is a dry cleaning carpet business.
Red wine stain removal and pet urine treatments.
Servicing all regional areas.
Updates

all logo and pictures files have been uploaded

Industry/Entity Type

Dry Cleaning

Contact Information for Business Card

Lumo-Fresh Carpet and upholstery cleaning.
Servicing Albury/Wodonga and surrounding areas.
ph gus 0461273904 ,email lumofresh1@tealpost.example

Font styles to use
Serif
Sans Serif
Other font styles liked:
• lumo fresh logo font

Colors
ec2027
ffcf3e
33a6d7
0692cd

Requirements
Nice to have
• I have included photos of the logo and car and stripe on van ,I dont need all of them in the card just i would like to stick to these colours.

```html
<!DOCTYPE html>
<html lang="en">
<head>
<meta charset="utf-8">
<title>Lumo-Fresh Business Card</title>
<link rel="stylesheet" href="https://fonts.googleapis.com/css2?family=Arimo:wght@400;700&display=swap">
<style>
  :root {
    --backdrop: #e4e4e4;
    --card: #ffffff;
    --brand-blue: #29a3ec;
    --ink-blue: #2343b3;
    --accent-yellow: #f4c73e;
    --accent-red: #f2564d;
    --ink-dark: #333333;
  }
  html, body {
    margin: 0;
    width: 1200px;
    height: 1000px;
    overflow: hidden;
    background: var(--backdrop);
    font-family: "Arimo", Arial, sans-serif;
  }
  .card {
    position: absolute;
    left: 75px;
    top: 200px;
    width: 1050px;
    height: 600px;
    background: var(--card);
    overflow: hidden;
    box-shadow: 0 6px 24px rgba(0,0,0,0.18);
  }
  .accent-area {
    position: absolute;
    inset: 0;
    width: 1050px;
    height: 600px;
  }
  .brand {
    position: absolute;
    left: 60px;
    top: 95px;
    width: 420px;
    text-align: center;
  }
  .brand-name {
    margin: 0;
    font-size: 62px;
    font-weight: 700;
    color: var(--brand-blue);
    letter-spacing: 1px;
  }
  .brand-tagline {
    margin: 10px 0 0;
    font-size: 25px;
    font-weight: 400;
    color: var(--ink-blue);
    text-transform: uppercase;
    line-height: 1.15;
  }
  .contact {
    position: absolute;
    left: 95px;
    top: 335px;
    margin: 0;
    padding: 0;
    list-style: none;
    font-size: 25px;
    color: var(--ink-dark);
  }
  .contact li {
    display: flex;
    align-items: center;
    gap: 16px;
    margin-bottom: 12px;
  }
  .contact svg { width: 20px; height: 20px; fill: var(--accent-yellow); }
  .service-area {
    position: absolute;
    left: 745px;
    top: 395px;
    width: 290px;
    margin: 0;
    text-align: center;
    font-size: 24px;
    color: var(--ink-blue);
    line-height: 1.2;
  }
</style>
</head>
<body>
  <main class="card">
    <svg class="accent-area" viewBox="0 0 1050 600" role="img" aria-label="Diagonal decorative band in the brand blue, yellow and red">
      <defs>
        <linearGradient id="accent-fade" x1="0" y1="0" x2="1" y2="0">
          <stop offset="0" stop-color="#29a3ec"/>
          <stop offset="0.55" stop-color="#f4c73e"/>
          <stop offset="1" stop-color="#f2564d"/>
        </linearGradient>
      </defs>
      <polygon points="730,0 990,0 600,600 440,600" fill="url(#accent-fade)"/>
    </svg>

    <header class="brand">
      <h1 class="brand-name">Lumo-Fresh</h1>
      <p class="brand-tagline">Carpet &amp; Upholstery<br>Cleaning</p>
    </header>

    <ul class="contact">
      <li>
        <svg viewBox="0 0 24 24" aria-hidden="true"><path d="M6.6 10.8a15.1 15.1 0 0 0 6.6 6.6l2.2-2.2a1 1 0 0 1 1-.25 11.4 11.4 0 0 0 3.6.57 1 1 0 0 1 1 1V20a1 1 0 0 1-1 1A17 17 0 0 1 3 4a1 1 0 0 1 1-1h3.5a1 1 0 0 1 1 1c0 1.25.2 2.45.57 3.6a1 1 0 0 1-.25 1z"/></svg>
        <span>0461273904</span>
      </li>
      <li>
        <svg viewBox="0 0 24 24" aria-hidden="true"><path d="M2 5h20v14H2z M2 5l10 8 10-8" stroke="#fff" stroke-width="1.5"/></svg>
        <span>lumofresh1@tealpost.example</span>
      </li>
    </ul>

    <p class="service-area">Servicing Albury/Wodonga<br>and surrounding areas</p>
  </main>
</body>
</html>
```